Full service meeting planning company needs new business cards

Velmora Linkway is a full service meeting planning company that specializes in on-line conference registration web development and event communications. We combine citywide hotel management, mobile applications, eblast reminders, confirmation letters, and customized reporting to create a seamless registration process. We also manage group motor coach transportation, food and beverages, entertainment, stage and lighting for group of 10 to 4000.

Target Market(s)

Corporations and associations

Industry/Entity Type

Event Planning

Contact Information for Business Card

standard size 3.5" wide and 2" tall

Font styles to use
Serif
Sans Serif

Colors
f37122
f78f20
333333
5c5c5c
9d9d9d
f68d4d

Requirements
Must have
• {name}
• Velmora Linkway
• P.O. Box 7384, Grand Rapids, M I 49568
• www.velmoralinkway.com
• {email}
• {phone}
• {mobile phone}
Nice to have
• Our colors are black, grey and orange as an accent color
Should not have
• I am not happy with our website layout anymore either. It feels dark and old but it does explain who we are pretty well if you'd like to review; www.velmoralinkway.com

```html
<!DOCTYPE html>
<html lang="en">
<head>
<meta charset="utf-8">
<title>Velmora Linkway – Business Card</title>
<link rel="stylesheet" href="https://fonts.googleapis.com/css2?family=Questrial&family=Roboto:wght@400&family=Khand:wght@600&display=swap">
<style>
  :root {
    --orange: #e27418;
    --orange-deep: #d96a12;
    --grey-dark: #5c5c5c;
    --grey-text: #4a4a4a;
    --paper: #f7f7f7;
    --stage: #ececec;
  }
  * { margin: 0; padding: 0; box-sizing: border-box; }
  html, body { width: 1200px; height: 443px; overflow: hidden; }
  body { background: var(--stage); position: relative; font-family: "Roboto", sans-serif; }

  .card { position: absolute; width: 484px; height: 292px; border-radius: 14px; overflow: hidden; }

  /* Front */
  .card-front { left: 81px; top: 72px; background: linear-gradient(180deg, var(--orange) 0%, var(--orange-deep) 100%); }
  .front-mark { position: absolute; left: 50%; top: 50%; transform: translate(-50%, -50%); display: flex; flex-direction: column; align-items: center; gap: 14px; }
  .front-mark .disc { width: 112px; height: 112px; border-radius: 50%; background: var(--grey-dark); }
  .front-mark .brand-name { font-family: "Questrial", sans-serif; font-size: 20px; letter-spacing: 1px; color: #ffffff; }

  /* Back */
  .card-back { left: 602px; top: 72px; background: var(--paper); }
  .brand { position: absolute; left: 25px; top: 29px; display: flex; align-items: center; gap: 10px; }
  .brand .disc { width: 58px; height: 58px; border-radius: 50%; background: var(--orange); }
  .brand .brand-name { font-family: "Questrial", sans-serif; font-size: 24px; letter-spacing: 0.5px; color: var(--grey-dark); }

  .person { position: absolute; right: 25px; top: 130px; text-align: right; color: var(--grey-text); }
  .person .name { font-family: "Khand", sans-serif; font-weight: 600; font-size: 22px; line-height: 1; }
  .person .role { font-size: 11.5px; margin-top: 4px; }

  .divider { position: absolute; left: 24px; top: 167px; width: 278px; height: 1px; background: var(--orange); }

  .contacts { position: absolute; left: 28px; top: 188px; list-style: none; font-size: 12.6px; color: var(--grey-text); }
  .contacts li { display: flex; align-items: center; height: 17.4px; }
  .contacts svg { width: 11px; height: 11px; margin-right: 10px; fill: var(--orange); flex: none; }

  .address { position: absolute; right: 25px; top: 205px; text-align: right; font-size: 12.6px; line-height: 17.4px; color: var(--grey-text); }

  .bands { position: absolute; left: 0; bottom: 0; width: 484px; height: 32px; }
</style>
</head>
<body>
  <section class="card card-front">
    <div class="front-mark">
      <div class="disc"></div>
      <div class="brand-name">VELMORA LINKWAY</div>
    </div>
  </section>

  <section class="card card-back">
    <div class="brand">
      <div class="disc"></div>
      <div class="brand-name">VELMORA LINKWAY</div>
    </div>

    <div class="person">
      <div class="name">Marissa Okafor</div>
      <div class="role">CMP, Sr. Project Manager</div>
    </div>

    <div class="divider"></div>

    <ul class="contacts">
      <li><svg viewBox="0 0 12 12"><path d="M1 4c0-2 2-3 5-3s5 1 5 3v1H8.5V3.8h-5V5H1zM2.5 6h7l1 5h-9z"/></svg>616 555 0148 x12</li>
      <li><svg viewBox="0 0 12 12"><path d="M3 1h6v3H3zM1 5h10v4H9v2H3V9H1zM4 8v2h4V8z"/></svg>616 555 0193</li>
      <li><svg viewBox="0 0 12 12"><path d="M1 2.5h10v7H1zM2 3.5l4 3 4-3v-.1H2z"/></svg>info@velmoralinkway.com</li>
      <li><svg viewBox="0 0 12 12"><path d="M6 1a5 5 0 1 0 0 10A5 5 0 0 0 6 1zm0 1c.7.8 1.1 2 1.2 3.5H4.8C4.9 4 5.3 2.8 6 2zM2.1 6.5h1.7c.1 1.2.4 2.2.9 3A4 4 0 0 1 2.1 6.5zm0-1a4 4 0 0 1 2.6-3c-.5.8-.8 1.8-.9 3zm2.7 1h2.4C7.1 8 6.7 9.2 6 10c-.7-.8-1.1-2-1.2-3.5zm3.4 0h1.7a4 4 0 0 1-2.6 3c.5-.8.8-1.8.9-3zm0-1c-.1-1.2-.4-2.2-.9-3a4 4 0 0 1 2.6 3z"/></svg>www.velmoralinkway.com</li>
    </ul>

    <div class="address">PO Box 7384<br>Grand Rapids, MI 49568</div>

    <svg class="bands" viewBox="0 0 484 32" preserveAspectRatio="none">
      <rect x="0" y="17" width="270" height="15" fill="var(--grey-dark)"/>
      <polygon points="276,2 484,2 484,32 253,32" fill="var(--orange-deep)"/>
    </svg>
  </section>
</body>
</html>
```